" Iniciamos o projeto do cliente com análise do consumo de energia elétrica, a partir disso dimensionamos o sistema utilizando a melhor solução de energia solar fotovoltaica para o cliente. Elaboramos a proposta do projeto com o orçamento e após aceite do cliente iniciamos o processo de homologação junto às concessionárias e instalação do sistema no cliente com a nossa própria equipe técnica. Também apresentamos o saving e payback do projeto. "

```html
<!DOCTYPE html>
<html lang="pt-BR">
<head>
<meta charset="utf-8">
<title>Radiare – Exemplo de usina solar fotovoltaica</title>
<link href="https://fonts.googleapis.com/css2?family=Montserrat:wght@600;800&family=Open+Sans:wght@400;600;700&display=swap" rel="stylesheet">
<style>
  :root{
    --navy:#16325c;
    --orange:#f07a1a;
    --ink:#2c2c2c;
    --muted:#6b6b6b;
    --green:#1f7a3a;
    --green-light:#7fc18f;
    --red:#b3282d;
    --red-light:#f0a9a6;
    --page:#eceeef;
    --white:#ffffff;
  }
  *{box-sizing:border-box;margin:0;padding:0}
  html,body{width:1200px;height:1200px;overflow:hidden;background:var(--page)}
  .slide{
    position:absolute;left:0;top:265px;width:1200px;height:670px;
    background:var(--white);font-family:"Open Sans",sans-serif;color:var(--ink);overflow:hidden;
  }
  .hero-photo{position:absolute;right:0;top:0;width:470px;height:112px}
  .brand{
    position:absolute;right:34px;top:24px;width:230px;height:66px;background:var(--white);
    display:flex;align-items:center;justify-content:center;gap:12px;
  }
  .brand-dot{width:26px;height:26px;border-radius:50%;background:var(--orange)}
  .brand-name{font-family:"Montserrat",sans-serif;font-weight:600;font-size:30px;color:var(--navy)}
  .example-title{position:absolute;left:140px;top:110px;font-family:"Montserrat",sans-serif;font-weight:800;font-size:33px;line-height:1.15}
  .example-title .accent{color:var(--orange);display:block}
  .example-title .main{color:var(--navy);display:block}
  .spec-list{position:absolute;left:150px;top:255px;list-style:none;border-left:4px solid var(--orange);padding-left:28px}
  .spec-list li{position:relative;font-size:19px;color:var(--muted);height:47px;line-height:28px}
  .spec-list li::before{
    content:"";position:absolute;left:-39px;top:7px;width:14px;height:14px;border-radius:50%;background:var(--orange);
  }
  .spec-list strong{color:var(--ink);font-weight:700}
  .spec-value{position:relative;display:inline-block}
  .spec-note{position:absolute;right:0;top:24px;font-size:9px;line-height:12px;color:var(--muted);white-space:nowrap}
  .invest-title{position:absolute;left:650px;top:270px;font-family:"Montserrat",sans-serif;font-weight:800;font-size:27px;line-height:1.2}
  .invest-title .accent{color:var(--orange);display:block}
  .invest-title .main{color:var(--navy);display:block}
  .compare-chart{position:absolute;left:650px;top:368px;width:520px;height:110px}
  .legend{position:absolute;left:650px;top:482px;display:flex;align-items:center;gap:12px;font-size:15px;font-weight:600;color:var(--navy)}
  .legend-swatch{width:80px;height:8px;border-radius:2px}
  .legend-swatch.solar{background:linear-gradient(90deg,var(--green),var(--green-light))}
  .legend-swatch.fixed-income{background:linear-gradient(90deg,var(--red),var(--red-light))}
  .legend-gap{width:14px}
  .body-copy{position:absolute;left:650px;top:520px;width:510px;font-size:12.5px;line-height:1.55;color:var(--muted)}
  .footer-band{position:absolute;left:0;bottom:0;width:100%;height:22px;background:var(--navy);border-top:3px solid var(--orange)}
</style>
</head>
<body>
<main class="slide">
  <svg class="hero-photo" viewBox="0 0 470 112" role="img" aria-label="Fotografia de painéis solares sob céu azul">
    <defs>
      <linearGradient id="panelsTone" x1="0" y1="0" x2="1" y2="1">
        <stop offset="0" stop-color="#8fb3d6"/>
        <stop offset="0.55" stop-color="#3f5f8e"/>
        <stop offset="1" stop-color="#1f355c"/>
      </linearGradient>
    </defs>
    <polygon points="34,0 470,0 470,112 0,112" fill="var(--navy)"/>
    <polygon points="52,0 470,0 470,112 20,112" fill="var(--orange)"/>
    <polygon points="66,0 470,0 470,112 36,112" fill="url(#panelsTone)"/>
  </svg>
  <div class="brand">
    <span class="brand-dot"></span>
    <span class="brand-name">Radiare</span>
  </div>

  <h1 class="example-title">
    <span class="accent">VEJA UM EXEMPLO DE</span>
    <span class="main">USINA SOLAR FOTOVOLTAICA:</span>
  </h1>

  <ul class="spec-list">
    <li>Tamanho da usina: <strong>20 painéis fotovoltaicos</strong></li>
    <li>Geração mensal média: <strong>750kWh</strong></li>
    <li>Economia Mensal: <strong>R$700,00</strong></li>
    <li>Custo do Sistema Implantado: <span class="spec-value"><strong>R$25.685,89</strong><span class="spec-note">R$/Wp ~ R$3,70</span></span></li>
    <li>Área ocupada (telhado): <strong>40m²</strong></li>
    <li>Payback: <strong>37 meses</strong> (tarifa ~ 1R$/ kWh)</li>
  </ul>

  <h2 class="invest-title">
    <span class="accent">O MELHOR INVESTIMENTO PARA</span>
    <span class="main">SUA EMPRESA OU SUA FAMÍLIA</span>
  </h2>

  <svg class="compare-chart" viewBox="0 0 520 110" role="img" aria-label="Comparação de rendimento: energia fotovoltaica contra renda fixa">
    <defs>
      <linearGradient id="greenBar" x1="0" x2="1">
        <stop offset="0" stop-color="#cfe8d4"/><stop offset="1" stop-color="#1f7a3a"/>
      </linearGradient>
      <linearGradient id="redBar" x1="0" x2="1">
        <stop offset="0" stop-color="#f3c5c2"/><stop offset="1" stop-color="#b3282d"/>
      </linearGradient>
    </defs>
    <rect x="2" y="18" width="505" height="22" rx="11" fill="#fff" stroke="#bdbdbd" stroke-width="2"/>
    <rect x="3" y="19" width="490" height="20" rx="10" fill="url(#greenBar)"/>
    <circle cx="492" cy="29" r="15" fill="#1f7a3a" stroke="#222" stroke-width="3"/>
    <rect x="2" y="64" width="505" height="22" rx="11" fill="#fff" stroke="#bdbdbd" stroke-width="2"/>
    <rect x="3" y="65" width="272" height="20" rx="10" fill="url(#redBar)"/>
    <circle cx="275" cy="75" r="15" fill="#b3282d" stroke="#222" stroke-width="3"/>
  </svg>

  <div class="legend">
    <span>Energia Fotovoltaica</span><span class="legend-swatch solar"></span>
    <span class="legend-gap"></span>
    <span>Renda fixa</span><span class="legend-swatch fixed-income"></span>
  </div>

  <p class="body-copy">Com a energia solar fotovoltaica, sua conta de luz cai já no primeiro mês e o sistema se paga em poucos anos. Depois disso, toda a economia gerada fica com você, por mais de vinte e cinco anos de vida útil dos painéis, com manutenção simples e baixo custo.</p>

  <div class="footer-band"></div>
</main>
</body>
</html>
```